Recycling Depot Business Card Design

We need a double sided business card for our recycling depot business. Please include name, position, address, phone, cell, fax, email and website address. Business card should match the colour scheme of our logo and look environmental but modern. I've attached a few business cards from Mintvale Works that I like.

Industry/Entity Type

Recycling

Contact Information for Business Card

Please include name, position, address, phone, cell, fax, email and website address.

Font styles to use
Sans Serif

Requirements
Must have
• Our Logo, Colour Scheme that matches our logo. Use of Colour Gradients and a custom look.

```html
<!DOCTYPE html>
<html lang="en">
<head>
<meta charset="utf-8">
<title>Greenloop Depot – Business Card</title>
<link href="https://fonts.googleapis.com/css2?family=Montserrat:wght@400;500;700&display=swap" rel="stylesheet">
<style>
  :root {
    --page-bg: #e6e9ec;
    --card-bg: #f3f5f4;
    --card-edge: #ffffff;
    --green-dark: #1d5e34;
    --green-mid: #2f7d3a;
    --green-light: #8cc43f;
    --ink: #1f2a24;
  }
  * { margin: 0; padding: 0; box-sizing: border-box; }
  html, body {
    width: 1200px; height: 970px; overflow: hidden;
    background: var(--page-bg);
    font-family: "Montserrat", sans-serif;
  }
  .card {
    position: absolute; left: 80px; top: 189px;
    width: 1040px; height: 592px;
    background: var(--card-bg);
    border: 2px solid var(--card-edge);
    border-radius: 28px;
    overflow: hidden;
    box-shadow: 0 10px 30px rgba(0,0,0,0.12);
  }
  .card-wave { position: absolute; left: 0; top: 0; width: 100%; height: 100%; }
  .brand {
    position: absolute; left: 46px; top: 268px;
    display: flex; align-items: center; gap: 16px;
  }
  .brand-dot {
    width: 44px; height: 44px; border-radius: 50%;
    background: var(--green-mid);
  }
  .brand-name {
    font-size: 44px; font-weight: 700; color: var(--green-dark);
    letter-spacing: -0.5px;
  }
  .divider {
    position: absolute; left: 520px; top: 118px;
    width: 2px; height: 356px; background: var(--green-mid);
  }
  .contact { position: absolute; left: 549px; top: 110px; color: var(--ink); }
  .contact-name {
    font-size: 35px; font-weight: 700; color: var(--green-dark);
    letter-spacing: 0.3px; line-height: 1.2;
  }
  .contact-role { font-size: 24px; font-weight: 400; margin-top: 2px; }
  .contact-address { font-size: 24px; line-height: 37px; margin-top: 20px; }
  .contact-lines { list-style: none; margin-top: 14px; }
  .contact-lines li {
    display: flex; align-items: center; gap: 8px;
    font-size: 24px; line-height: 37px;
  }
  .contact-lines svg { width: 22px; height: 22px; flex: none; fill: var(--green-mid); }
</style>
</head>
<body>
  <div class="card">
    <svg class="card-wave" viewBox="0 0 1475 840" preserveAspectRatio="none" aria-hidden="true">
      <defs>
        <linearGradient id="swoosh" x1="0" x2="1" y1="0" y2="0">
          <stop offset="0" stop-color="#5f9e34" stop-opacity="0.2"/>
          <stop offset="0.6" stop-color="#8cc43f"/>
          <stop offset="1" stop-color="#6fae3a"/>
        </linearGradient>
        <linearGradient id="band" x1="0" x2="1" y1="0" y2="0">
          <stop offset="0" stop-color="#1f6a38"/>
          <stop offset="1" stop-color="#1a5a30"/>
        </linearGradient>
      </defs>
      <path d="M380 752 C 800 790, 1150 740, 1475 700 L1475 740 C 1150 765, 800 790, 380 752 Z" fill="url(#swoosh)"/>
      <path d="M0 735 C 400 760, 900 805, 1475 755 L1475 840 L0 840 Z" fill="url(#band)"/>
    </svg>

    <div class="brand">
      <span class="brand-dot"></span>
      <span class="brand-name">Greenloop Depot</span>
    </div>

    <div class="divider"></div>

    <div class="contact">
      <h1 class="contact-name">DANIEL HARTLEY</h1>
      <p class="contact-role">President</p>
      <p class="contact-address">1840 Cedar Hollow Road<br>Suite 210 Fernbrook, CA 90000</p>
      <ul class="contact-lines">
        <li><svg viewBox="0 0 24 24"><path d="M3 9c0-3 4-5 9-5s9 2 9 5v2h-5V9H8v2H3z M6 12h12l2 8H4z"/></svg>+31 555-014-2200</li>
        <li><svg viewBox="0 0 24 24"><path d="M7 2h10a1 1 0 0 1 1 1v18a1 1 0 0 1-1 1H7a1 1 0 0 1-1-1V3a1 1 0 0 1 1-1zm1 3v13h8V5z"/></svg>+31 555-014-2201</li>
        <li><svg viewBox="0 0 24 24"><path d="M7 3h10v5H7z M4 9h16v8h-3v4H7v-4H4z M9 14v5h6v-5z"/></svg>+31 555-014-2202</li>
        <li><svg viewBox="0 0 24 24"><path d="M2 6h20v12H2z M2 6l10 7 10-7" stroke="#f3f5f4" stroke-width="1.5"/></svg>info@greenloopdepot.com</li>
        <li><svg viewBox="0 0 24 24"><circle cx="12" cy="12" r="10"/><path d="M2 12h20M12 2c3 3 3 17 0 20M12 2c-3 3-3 17 0 20" stroke="#f3f5f4" stroke-width="1.3" fill="none"/></svg>www.greenloopdepot.com</li>
      </ul>
    </div>
  </div>
</body>
</html>
```